Zielgruppe
Der Bohnenglanz GmbH ist spezialisiert auf hochwertigen Kaffee und bietet exklusive Röstungen für anspruchsvolle Geniesser. Als Kaffee-Sommelier lege ich besonderen Wert auf Qualität, Nachhaltigkeit und Transparenz – vom Rohkaffee bis zur perfekten Tasse. Neben dem Verkauf von Spezialitätenkaffee biete ich auch Schulungen, Verkostungen und individuelle Beratung für Unternehmen und Privatkunden an.
Aufgabenstellung
Eine neue Produkte-Linie soll entstehen. Dabei soll erkennbar sein, dass die neuen Produkte optisch zur Produkte Linie Kaffee passen und den selben Charakter haben aber trotzdem etwas anderes ist. Nämlich Tee statt Kaffee und daher optisch sich von der Kaffee Linie unterscheidet.
Die neue Produkte Linie heisst Mo.Lu
HAUPTETIKETT (Vorderseite) 9.5 x 12.5 cm
Eckenrundung mit 3 mm Radius
1. Tirsa Melo – Das Erbe von Hashara
Kaffee-Infusion aus ungerösteten Kaffeebohnen und Gewürzen
Beschreibung:
In Äthiopiens alten Handelsstädten war Hashara, Tee aus ungerösteten Kaffeebohnen, ein belebendes Getränk für Händler. Tirsa Melo lässt diese Tradition neu aufleben – mit milder Frische und erlesenen Gewürzen aus Afrikas und Orients Karawanenwegen.
Zutaten:
Ungeröstete Kaffeebohnen
Hibiskusblüten
Zimt
Zitronengras
Basilikum
Süssholzwurzel
Enthält Koffein
Brühtemperatur: 100°C
Ziehzeit: 8 Minuten
2. Velora Tisan – Die verborgene Weisheit des Dschungels
Kaffee-Infusion aus Kaffeeblättern und exotischen Aromen
In Sumatras Wäldern war Kopi Daun, der Tee aus Kaffeeblättern, ein gut gehütetes Geheimnis der Einheimischen. Velora Tisan vereint diese Tradition mit exotischen Gewürzen des Malaiischen Archipels zu einem sinnlichen Erlebnis.
Kaffeeblätter
Ingwer
Galgant
Kurkuma
Bunter Pfeffer
Kardamom
Brühtemperatur: 95°C
Ziehzeit: 6 Minuten
3. Luma Verana – Das Gold der Anden
Kaffee-Infusion aus Cascara und feinen Gewürzen
Die Kaffeebauern der Anden schätzten Cascara – die getrocknete Kaffeekirsche – für erfrischende Aufgüsse. Luma Verana vereint sie mit ausgewählten Zutaten zu einem warmen, fruchtig-schokoladigen Genuss.
C..

```html
<!DOCTYPE html>
<html lang="de">
<head>
<meta charset="utf-8">
<title>Mo.Lu – Etiketten</title>
<link href="https://fonts.googleapis.com/css2?family=Bebas+Neue&family=Roboto+Condensed:wght@400;700&display=swap" rel="stylesheet">
<style>
  :root{
    --bg:#ffffff;
    --label:#0d0d0d;
    --text:#f2f2f2;
    --muted:#cfcfcf;
    --gold:#b8912a;
    --green:#8db33f;
    --sand:#c9b07a;
    --brown:#9a7150;
  }
  *{box-sizing:border-box;margin:0;padding:0}
  html,body{width:846px;height:1200px;overflow:hidden;background:var(--bg)}
  .sheet{position:relative;width:846px;height:1200px}
  .label{
    position:absolute;width:250px;height:322px;border-radius:12px;
    background:var(--label);color:var(--text);
    font-family:"Roboto Condensed",sans-serif;text-align:center;overflow:hidden;
  }
  .label--gold{--accent:var(--gold)}
  .label--green{--accent:var(--green)}
  .label--sand{--accent:var(--sand)}
  .label--brown{--accent:var(--brown)}
  .brand-tab{
    position:absolute;left:50%;top:0;transform:translateX(-50%);
    width:58px;height:44px;background:var(--accent);
    border-radius:0 0 29px 29px;display:flex;align-items:center;justify-content:center;
    font-family:"Roboto Condensed",sans-serif;font-weight:700;font-size:13px;color:#111;
  }
  .tagline{position:absolute;top:62px;left:0;right:0;font-size:6.5px;color:var(--accent)}
  .rule{position:absolute;left:0;right:0;height:0;border-top:1.5px dashed #777}
  .rule--top{top:75px}
  .rule--bottom{top:138px}
  .title{
    position:absolute;top:84px;left:0;right:0;
    font-family:"Bebas Neue",sans-serif;font-size:38px;line-height:1;letter-spacing:.5px;
  }
  .subtitle{
    position:absolute;top:121px;left:0;right:0;
    font-family:"Bebas Neue",sans-serif;font-size:13px;line-height:1;
  }
  .ingredients{position:absolute;top:150px;left:12px;right:12px;font-size:6.3px;line-height:1.45;text-transform:uppercase}
  .ingredients .head{display:block}
  .divider{width:70px;height:1px;background:var(--accent);margin:5px auto 0}
  .story{position:absolute;top:192px;left:20px;right:20px;font-size:4.9px;line-height:1.6;color:var(--muted)}
  .info-band{
    position:absolute;left:38px;width:174px;height:48px;bottom:12px;
    background:var(--accent);color:#111;display:flex;align-items:center;
  }
  .brew{width:52px;display:flex;align-items:center;justify-content:center;font-size:5px;line-height:1.2}
  .brew svg{width:26px;height:26px}
  .seal-slot{width:70px;height:100%;position:relative;border-left:1px solid rgba(0,0,0,.4);border-right:1px solid rgba(0,0,0,.4)}
  .seal{position:absolute;left:50%;top:-10px;transform:translateX(-50%);width:34px;height:34px;border-radius:50%;background:#d9c89a;border:2px solid #f0e6c8}
  .url{position:absolute;bottom:5px;left:0;right:0;font-size:4.6px;font-weight:700}
  .facts{flex:1;display:flex;flex-direction:column;align-items:center;gap:6px}
  .facts .caffeine{font-size:5.5px;font-weight:700}
  .facts .weight{font-size:8.5px}
</style>
</head>
<body>
<main class="sheet">

  <article class="label label--gold" style="left:31px;top:277px">
    <div class="brand-tab">Mo.Lu</div>
    <p class="tagline">Kaffee-Infus aus ungerösteten Kaffeebohnen und Gewürzen</p>
    <div class="rule rule--top"></div>
    <h2 class="title">Tirsa Melo</h2>
    <p class="subtitle">Das Erbe von Hashara</p>
    <div class="rule rule--bottom"></div>
    <p class="ingredients"><span class="head">Zutaten:</span>Ungeröstete Kaffeebohnen, Hibiskusblüten, Zimt<br>Zitronengras, Basilikum, Süssholzwurzel<span class="divider" style="display:block"></span></p>
    <p class="story">In den alten Handelsstädten Äthiopiens war Hashara, der Tee aus ungerösteten Kaffeebohnen, ein traditionelles, belebendes Getränk für Händler und Nomaden. Tirsa Melo – benannt nach den lebhaften Kaffeevierteln – bringt diese Tradition zurück. Die milde, fruchtige Frische der Bohnen verbindet sich mit erlesenen Gewürzen aus den Karawanenwegen Afrikas und des Orients.</p>
    <div class="info-band">
      <div class="brew"><svg viewBox="0 0 30 30"><path d="M5 13h16v6a6 6 0 0 1-6 6h-4a6 6 0 0 1-6-6z" fill="none" stroke="#111" stroke-width="1.3"/><path d="M21 15h2a3 3 0 0 1 0 6h-2" fill="none" stroke="#111" stroke-width="1.3"/><path d="M10 5c-2 2 2 3 0 6M15 5c-2 2 2 3 0 6" fill="none" stroke="#111" stroke-width="1"/><text x="13" y="21" font-size="4.5" text-anchor="middle" font-family="Roboto Condensed,sans-serif">95°C</text></svg></div>
      <div class="seal-slot"><div class="seal"></div><div class="url">www.bohnenglanz.ch</div></div>
      <div class="facts"><span class="caffeine">Enthält Koffein</span><span class="weight">200 gr</span></div>
    </div>
  </article>

  <article class="label label--green" style="left:295px;top:330px">
    <div class="brand-tab">Mo.Lu</div>
    <p class="tagline">Kaffee-Infus aus Kaffeeblättern und exotischen Aromen</p>
    <div class="rule rule--top"></div>
    <h2 class="title">Velora Tisan</h2>
    <p class="subtitle">Die verborgene Weisheit des Dschungels</p>
    <div class="rule rule--bottom"></div>
    <p class="ingredients"><span class="head">Zutaten:</span>Kaffeeblätter, Gunpowder Grüntee, Ingwer, Galgant,<br>Bunter Pfeffer, Kardamom, Kurkuma<span class="divider" style="display:block"></span></p>
    <p class="story" style="font-size:5.3px">In Sumatras Wäldern war Kopi Daun, der Tee aus Kaffeeblättern, ein gut gehütetes Geheimnis der Einheimischen. Velora Tisan vereint diese Tradition mit exotischen Gewürzen des Malaiischen Archipels zu einem sinnlichen Erlebnis.</p>
    <div class="info-band">
      <div class="brew"><svg viewBox="0 0 30 30"><path d="M5 13h16v6a6 6 0 0 1-6 6h-4a6 6 0 0 1-6-6z" fill="none" stroke="#111" stroke-width="1.3"/><path d="M21 15h2a3 3 0 0 1 0 6h-2" fill="none" stroke="#111" stroke-width="1.3"/><path d="M10 5c-2 2 2 3 0 6M15 5c-2 2 2 3 0 6" fill="none" stroke="#111" stroke-width="1"/><text x="13" y="21" font-size="4.5" text-anchor="middle" font-family="Roboto Condensed,sans-serif">90°C</text></svg></div>
      <div class="seal-slot"><div class="seal"></div><div class="url">www.bohnenglanz.ch</div></div>
      <div class="facts"><span class="caffeine">Enthält Koffein</span><span class="weight">200 gr</span></div>
    </div>
  </article>

  <article class="label label--sand" style="left:563px;top:467px">
    <div class="brand-tab">Mo.Lu</div>
    <p class="tagline">Kaffee-Infus aus Cascara und feinen Gewürzen</p>
    <div class="rule rule--top"></div>
    <h2 class="title">Luma Verana</h2>
    <p class="subtitle">Das Gold der Anden</p>
    <div class="rule rule--bottom"></div>
    <p class="ingredients"><span class="head">Zutaten:</span>Cascara (Kaffeekirschen-Schalen), Kakaoschalen, Orangenschalen, Zimt</p>
    <p class="story" style="top:180px;font-size:5.3px">Die Kaffeebauern der Anden schätzten Cascara – die getrocknete Kaffeekirsche – für erfrischende Aufgüsse. Luma Verana vereint sie mit ausgewählten Zutaten zu einem warmen, fruchtig-schokoladigen Genuss.</p>
    <div class="info-band">
      <div class="brew"><svg viewBox="0 0 30 30"><path d="M5 13h16v6a6 6 0 0 1-6 6h-4a6 6 0 0 1-6-6z" fill="none" stroke="#111" stroke-width="1.3"/><path d="M21 15h2a3 3 0 0 1 0 6h-2" fill="none" stroke="#111" stroke-width="1.3"/><path d="M10 5c-2 2 2 3 0 6M15 5c-2 2 2 3 0 6" fill="none" stroke="#111" stroke-width="1"/><text x="13" y="21" font-size="4.5" text-anchor="middle" font-family="Roboto Condensed,sans-serif">85°C</text></svg></div>
      <div class="seal-slot"><div class="seal"></div><div class="url">www.bohnenglanz.ch</div></div>
      <div class="facts"><span class="caffeine">Enthält Koffein</span><span class="weight">200 gr</span></div>
    </div>
  </article>

  <article class="label label--brown" style="left:30px;top:620px">
    <div class="brand-tab">Mo.Lu</div>
    <p class="tagline">Kaffee-Infus mit gerösteten Kaffeebohnen und Schweizer Kräutern</p>
    <div class="rule rule--top"></div>
    <h2 class="title">Alpina Nocca</h2>
    <p class="subtitle">Kaffee und Alpengeheimnisse</p>
    <div class="rule rule--bottom"></div>
    <p class="ingredients"><span class="head">Zutaten:</span>Geröstete Kaffeebohnen, Malvenblüten, Brombeerblätter<br>Lindenblüten, Hagebutte, Thymian</p>
    <p class="story" style="top:186px;font-size:5px">1615 gelangte Kaffee über Handelsrouten in die Schweiz und traf auf die alte Kräutertradition des Landes. Alpina Nocca vereint diese Verbindung in einer einzigartigen Mischung aus gerösteten Kaffeebohnen und handgepflückten Schweizer Kräutern.</p>
    <div class="info-band">
      <div class="brew"><svg viewBox="0 0 30 30"><path d="M5 13h16v6a6 6 0 0 1-6 6h-4a6 6 0 0 1-6-6z" fill="none" stroke="#111" stroke-width="1.3"/><path d="M21 15h2a3 3 0 0 1 0 6h-2" fill="none" stroke="#111" stroke-width="1.3"/><path d="M10 5c-2 2 2 3 0 6M15 5c-2 2 2 3 0 6" fill="none" stroke="#111" stroke-width="1"/><text x="13" y="21" font-size="4.5" text-anchor="middle" font-family="Roboto Condensed,sans-serif">95°C</text></svg></div>
      <div class="seal-slot"><div class="seal"></div><div class="url">www.bohnenglanz.ch</div></div>
      <div class="facts"><span class="caffeine">Enthält Koffein</span><span class="weight">200 gr</span></div>
    </div>
  </article>

</main>
</body>
</html>
```